Business Card Design Project

We are rebranding an existing automotive collision repair business. The business is called harrowell works. I have attached logo but I'm not tied to that. I want to leave this wide open.

I want this card to say we are professional, competent, cutting edge. We are focused on customers and use a lot of the latest technology to make the customer experience different. We sign customers in on Vextabs. Paperwork I signed electronically and updates are sent via text, email, logging on a website or as they wish. I want this innovation and image to come through in our cards

Target Market(s)

60%. Women 40% men. Age 35-60

Industry/Entity Type

Automotive

Requirements
Must have
• The card must have name, title, phone,email, cell, web page

```html
<!DOCTYPE html>
<html lang="en">
<head>
<meta charset="utf-8">
<title>harrowell works — business card</title>
<link rel="stylesheet" href="https://fonts.googleapis.com/css2?family=Mulish:wght@400;600;800&display=swap">
<style>
  :root {
    --backdrop: #3a3a3a;
    --card-dark: #0b0b0b;
    --card-light: #f4f4f2;
    --brand-green: #8cc63f;
    --ink-dark: #1c1c1c;
    --ink-mid: #5a5a5a;
    --ink-on-dark: #e6e6e6;
  }
  * { box-sizing: border-box; margin: 0; padding: 0; }
  html, body {
    width: 1200px; height: 900px; overflow: hidden;
    background: var(--backdrop);
    font-family: "Mulish", sans-serif;
  }
  .card {
    position: absolute;
    left: 268px;
    width: 664px; height: 380px;
    border-radius: 2px;
    box-shadow: 0 14px 30px rgba(0,0,0,.45);
    overflow: hidden;
  }
  .card--back {
    top: 46px;
    background: linear-gradient(150deg, #1a1a1a 0%, var(--card-dark) 55%);
  }
  .card--front {
    top: 474px;
    background: var(--card-light);
  }
  .wordmark {
    font-weight: 800;
    color: var(--brand-green);
    letter-spacing: -0.5px;
    white-space: nowrap;
  }
  .card--back .wordmark {
    position: absolute; left: 0; right: 0; top: 150px;
    text-align: center; font-size: 46px;
  }
  .card--back .web {
    position: absolute; right: 48px; bottom: 40px;
    color: var(--ink-on-dark); font-size: 15px; letter-spacing: .5px;
  }
  .card--front .wordmark {
    position: absolute; left: 40px; top: 168px;
    font-size: 36px;
  }
  .contact {
    position: absolute; left: 392px; top: 0; bottom: 0; right: 0;
    padding: 58px 0 0 34px;
    background: linear-gradient(90deg, rgba(0,0,0,.06), rgba(0,0,0,0) 30px);
  }
  .contact__name { font-size: 19px; font-weight: 800; color: var(--ink-dark); }
  .contact__role { font-size: 14px; color: var(--brand-green); margin-top: 2px; }
  .contact__address {
    font-style: normal; font-size: 15px; font-weight: 600;
    color: var(--ink-mid); line-height: 1.3; margin-top: 24px;
  }
  .contact__lines { list-style: none; margin-top: 22px; }
  .contact__lines li {
    display: flex; align-items: center; gap: 9px;
    font-size: 15px; color: var(--ink-mid); line-height: 1.35;
    white-space: nowrap;
  }
  .contact__lines svg { width: 13px; height: 13px; fill: var(--brand-green); flex: none; }
</style>
</head>
<body>
  <section class="card card--back">
    <div class="wordmark">harrowell works</div>
    <div class="web">www.harrowellworks.com</div>
  </section>

  <section class="card card--front">
    <div class="wordmark">harrowell works</div>
    <div class="contact">
      <div class="contact__name">Dana Merrow</div>
      <div class="contact__role">Position</div>
      <address class="contact__address">1234 Your Street Suite 123<br>City Name CA 12345</address>
      <ul class="contact__lines">
        <li>
          <svg viewBox="0 0 16 16" aria-label="Phone"><path d="M1 5c0-2 2-3 7-3s7 1 7 3v1h-4V4.5H5V6H1zM4 7h8l2 7H2z"/></svg>
          (123) 456-7890
        </li>
        <li>
          <svg viewBox="0 0 16 16" aria-label="Cell"><path fill-rule="evenodd" d="M5 0h6a1.5 1.5 0 0 1 1.5 1.5v13A1.5 1.5 0 0 1 11 16H5a1.5 1.5 0 0 1-1.5-1.5v-13A1.5 1.5 0 0 1 5 0zM5 2v10h6V2zM8 12.6a.9.9 0 1 0 0 1.8.9.9 0 0 0 0-1.8z"/></svg>
          (123) 456-7891
        </li>
        <li>
          <svg viewBox="0 0 16 16" aria-label="Email"><path d="M1 3h14v10H1zM2.5 4.5 8 9l5.5-4.5z" fill-rule="evenodd"/></svg>
          info@harrowellworks.com
        </li>
      </ul>
    </div>
  </section>
</body>
</html>
```